Vel Moro A4 paper and card metallic new packaging

Vel Moro New Packaging Brief
We need a CLASSIC packaging design which wraps around the bottom left side of the product (A4 card) in the shape of a square (front & back) for an existing brand name call Vel Moro. This is then covered in a polybag. This needs to display the most important detail about the product on the FRONT and then the other information on the back.
See images attached of some ideas
The packaging needs to be CLEAN and simple to portray the fact the product is of a Premium Luxurious quality.
It is sold in a store where it sits on a shelf so we need the following information portrayed very clearly so the consumer can see it straight away and know what the product is:
The below points need to be shown on the FRONT of the packaging - Information is listed in order of importance.
1.Premium Luxurious Card
2. Metallic
3. A4
4.The Colour (eg, Silver)
5.25 Pack
6. Logo – this can be small

These need to be shown on the BACK of the packaging - Information is listed in order of importance.
1.PREMIUM Luxurious Card
2.
• Ideal for card making for all occasions
• Invitations for all Celebrations
• Creative card & paper for presentations
3. Acid free
4. Made in china
5. Logo – this can be small
6.Barcode

Background
Vel Moro is a brand which sells PREMIUM Luxurious Paper and card stock which can be used for card making, invites, presentations. The colour range is approx. 24 colours and it comes in metallic and weave. It includes the following
*A4 Card 260gsm & paper 120gsm
*DL & C6 envelopes 120gsm

PLEASE READ ALL UPLOADED FILE NAMES.

Target Market(s)

Office supply and invitation market

Industry/Entity Type

Store

Requirements
Must have
• Most important is to have a style of packaging that suits and displays the product. Needs to be fresh and clean packaging but also show quality and show the actual product.
• Font should be simple, easy to read, clear so consumers can read what the product is straight away.
• Colours – can match the logo but we are open to other ideas as well.
• The colour range of the card we sell is 24 different colours so the actual packaging needs to match all colours and stand out.

```html
<!DOCTYPE html>
<html lang="en">
<head>
<meta charset="utf-8">
<title>Vel Moro Metallic Card Packaging</title>
<link href="https://fonts.googleapis.com/css2?family=Poiret+One&display=swap" rel="stylesheet">
<style>
  :root {
    --page: #fefefe;
    --card-top: #fafafa;
    --card-bottom: #f2f2f2;
    --wrap: #000000;
    --ink: #ffffff;
    --brand-ink: #8a8a8a;
    --gold-light: #f3e3a0;
    --gold-mid: #c9a42f;
    --gold-dark: #9c7a1c;
  }
  html, body {
    margin: 0;
    padding: 0;
    width: 1200px;
    height: 1000px;
    overflow: hidden;
    background: var(--page);
  }
  .canvas {
    position: relative;
    width: 1200px;
    height: 1000px;
    font-family: "Poiret One", sans-serif;
  }
  .card-sheet {
    position: absolute;
    left: 417px;
    top: 0;
    width: 783px;
    height: 676px;
    background: linear-gradient(180deg, var(--card-top), var(--card-bottom));
  }
  .wrap-front {
    position: absolute;
    left: 420px;
    top: 321px;
    width: 358px;
    height: 358px;
    background: var(--wrap);
    color: var(--ink);
    overflow: hidden;
  }
  .colour-swatch {
    position: absolute;
    left: 4px;
    top: 5px;
    width: 59px;
    height: 43px;
    background: linear-gradient(90deg, var(--gold-light) 0%, var(--gold-mid) 35%, var(--gold-light) 60%, var(--gold-dark) 100%);
  }
  .brand {
    position: absolute;
    left: 0;
    right: 0;
    top: 62px;
    display: flex;
    align-items: center;
    justify-content: center;
    gap: 10px;
    color: var(--brand-ink);
    font-size: 30px;
  }
  .brand-dot {
    width: 22px;
    height: 22px;
    border-radius: 50%;
    border: 1px solid var(--brand-ink);
  }
  .product-title {
    position: absolute;
    left: -20px;
    width: 398px;
    top: 142px;
    margin: 0;
    font-weight: 400;
    text-align: center;
    font-size: 37px;
    white-space: nowrap;
    transform: scaleX(0.92);
    transform-origin: center;
  }
  .size {
    position: absolute;
    left: 50px;
    top: 209px;
    font-size: 79px;
    line-height: 1;
    transform: scaleX(0.8);
    transform-origin: left top;
  }
  .finish {
    position: absolute;
    left: 185px;
    top: 213px;
    font-size: 38px;
    line-height: 1;
    white-space: nowrap;
    transform: scaleX(0.83);
    transform-origin: left top;
  }
  .pack-count {
    position: absolute;
    left: 54px;
    top: 311px;
    font-size: 25px;
    line-height: 1;
    white-space: nowrap;
  }
  .colour-name {
    position: absolute;
    left: 180px;
    top: 283px;
    font-size: 52px;
    line-height: 1;
    transform: scaleX(1.1);
    transform-origin: left top;
    background: linear-gradient(180deg, var(--gold-mid) 0%, var(--gold-light) 45%, var(--gold-mid) 70%, var(--gold-dark) 100%);
    -webkit-background-clip: text;
    background-clip: text;
    color: transparent;
  }
</style>
</head>
<body>
  <div class="canvas">
    <div class="card-sheet"></div>
    <section class="wrap-front">
      <div class="colour-swatch"></div>
      <div class="brand"><span class="brand-dot"></span><span>Vel Moro</span></div>
      <h1 class="product-title">Premium Luxurious Card</h1>
      <div class="size">A4</div>
      <div class="finish">Metallic</div>
      <div class="pack-count">25 Pack</div>
      <div class="colour-name">Gold</div>
    </section>
  </div>
</body>
</html>
```